DL size flyer for Autism Consultancy website

We need a printed flyer DL size ( 210mmx99mm) for our Autism Consultancy website www.brightpathkids.nz which provides therapy for autistic children.
I want the flyer to look consistent with the website’s design. Please feel free to use the colour scheme, fonts, icons or any images from www.brightpathkids.nz.It should be easy to see “Autism” or “Autistic” word from a distance.
Please use either an oversized logo or make “Do you have a verbal and able autistic child?” more prominent.
Please do not convert the text fields to outlines, i.e. I need to be able to edit any text after.The final design should be either in Adobe Illustrator or Adobe Photoshop format.
The Specs for the flyer are
Document Trim Size99 x 210 mm 1169 x 2480 pixels
Full Bleed Size102 x 213 mm 1205 x 2516 pixels
Our Logo https://1drv.ms/u/s!AoH0rRjDY2GYg6QtU-xjoVlmslKp6gPlease
use this photo for the front side https://qzdropbin.io/f/Pw4KcN8rTyH2mXs6BvLd9QeFz1Gj
another one for reverse
https://qzdropbin.io/f/Rk2HsV5nWqJ7tZc3MfXb8LpYd4Ne
Please use the following content:
Do you have a verbal and able autistic child?
We use child-centred, modern and innovative approaches
Teaching autistic children to bond, laugh and play.
We work with schools
We help autistic children to develop social minds
We offer:
• Specialist assessments
• Consultations for parents & schools
• Social learning programmes
• Social-cognitive therapy
We can create an individual learning path, best suited for your child.
Our programmes and interventions include:
• Chatter Quest
• Peer Bright
• Team Puzzles
• Tingle Words
• Pebble Tales
• Pembrook Speech Ladder
• Vorlin Method
• BRIMLE Method
• Tandem Pattern Coaching
contact details on both sides:
www.brightpathkids.nz
info@brightpathkids.nz
(09) 57-318-46

```html
<!DOCTYPE html>
<html lang="en">
<head>
<meta charset="utf-8">
<title>Bright Path Kids – DL Flyer</title>
<link rel="stylesheet" href="https://fonts.googleapis.com/css2?family=Fira+Sans+Extra+Condensed:wght@600;700&family=Roboto:wght@400&display=swap">
<style>
  :root {
    --navy: #1f2a57;
    --yellow: #fdcb0a;
    --teal: #55c4bd;
    --paper: #ececec;
    --white: #ffffff;
    --stage: #cfcfcf;
    --grey-text: #8a8a8a;
  }
  * { margin: 0; padding: 0; box-sizing: border-box; }
  html, body { width: 1200px; height: 1200px; overflow: hidden; }
  body { background: var(--stage); position: relative; font-family: "Roboto", sans-serif; }

  .flyer { position: absolute; top: 82px; width: 496px; height: 1036px; overflow: hidden; }
  .flyer--front { left: 74px; }
  .flyer--back { left: 645px; }
  .flyer__bg { position: absolute; inset: 0; width: 100%; height: 100%; }

  .display { font-family: "Fira Sans Extra Condensed", sans-serif; font-weight: 700; letter-spacing: 1.5px; }

  .brand { position: absolute; display: flex; align-items: center; gap: 14px; }
  .brand__mark { width: 64px; height: 64px; border-radius: 50%; background: var(--navy); flex: none; }
  .brand__name { font-family: "Fira Sans Extra Condensed", sans-serif; font-weight: 700; font-size: 40px; color: var(--navy); letter-spacing: 1px; white-space: nowrap; }
  .flyer--front .brand { left: 58px; top: 38px; }
  .flyer--back .brand { left: 72px; top: 890px; }

  .headline { position: absolute; left: 20px; width: 476px; top: 530px; text-align: center; color: var(--white); line-height: 1.05; }
  .headline__small { display: block; font-size: 33px; }
  .headline__mid { display: block; font-size: 36px; margin-top: 4px; }
  .headline__big { display: block; font-size: 58px; margin-top: 2px; letter-spacing: 2.5px; }

  .offer-title { position: absolute; left: 86px; top: 726px; font-size: 26px; color: var(--navy); }
  .programmes-title { position: absolute; left: 67px; top: 64px; font-size: 31px; line-height: 36px; color: var(--yellow); }

  .bullets { position: absolute; list-style: none; font-size: 17.5px; }
  .bullets li { display: flex; align-items: center; gap: 9px; }
  .bullets svg { width: 17px; height: 17px; flex: none; }
  .bullets--offer { left: 97px; top: 774px; color: var(--navy); }
  .bullets--offer li { height: 31px; }
  .bullets--offer svg { fill: var(--navy); }
  .bullets--programmes { left: 93px; top: 152px; color: var(--white); }
  .bullets--programmes li { height: 34.4px; }
  .bullets--programmes svg { fill: var(--yellow); }

  .contact { position: absolute; color: var(--white); }
  .contact__phone { display: flex; align-items: center; gap: 14px; }
  .contact__icon { width: 50px; height: 50px; border-radius: 50%; background: var(--navy); display: flex; align-items: center; justify-content: center; }
  .contact__icon svg { width: 26px; height: 26px; fill: var(--yellow); }
  .contact__number { font-size: 34px; letter-spacing: 3px; }
  .contact__line { display: flex; align-items: center; gap: 10px; font-size: 17.5px; line-height: 25px; }
  .contact__line svg { width: 20px; height: 16px; flex: none; stroke: var(--white); fill: none; stroke-width: 1.6; }
  .flyer--front .contact { left: 73px; top: 922px; }
  .flyer--front .contact__line { margin-left: 62px; }
  .flyer--back .contact { left: 125px; top: 490px; }
  .flyer--back .contact__line { margin-left: 62px; }
</style>
</head>
<body>

<svg width="0" height="0" style="position:absolute" aria-hidden="true">
  <defs>
    <symbol id="icon-puzzle" viewBox="0 0 20 20">
      <g transform="rotate(-20 10 10)">
        <rect x="3" y="6" width="11" height="11" rx="1"/>
        <circle cx="8.5" cy="5" r="3"/>
        <circle cx="15" cy="11.5" r="3"/>
      </g>
    </symbol>
    <symbol id="icon-phone" viewBox="0 0 24 24">
      <path d="M7 2.5c.8-.4 1.6 0 2 .8l1.6 3.4c.3.7.1 1.5-.5 1.9l-1.4 1c.8 2.4 2.3 4.6 4.3 6.3l1.5-.9c.6-.4 1.4-.3 1.9.3l2.4 2.8c.5.6.5 1.5-.1 2l-1.7 1.4c-1 .8-2.4 1-3.6.3C8.200 19.300 4.500 13.500 4.400 7.600c0-1.300.7-2.500 1.800-3.100z"/>
    </symbol>
    <symbol id="icon-mail" viewBox="0 0 20 16">
      <rect x="1" y="2" width="18" height="12"/>
      <path d="M1 2l9 7 9-7M1 14l7-6M19 14l-7-6"/>
    </symbol>
    <symbol id="icon-globe" viewBox="0 0 20 20">
      <circle cx="10" cy="10" r="8"/>
      <ellipse cx="10" cy="10" rx="3.5" ry="8"/>
      <path d="M2 10h16M3.500 5.500h13M3.500 14.500h13"/>
    </symbol>
    <linearGradient id="photo-front" x1="0" y1="0" x2="1" y2="1">
      <stop offset="0" stop-color="#efefef"/>
      <stop offset="0.45" stop-color="#e6ddd0"/>
      <stop offset="0.75" stop-color="#d9a27a"/>
      <stop offset="1" stop-color="#efe6da"/>
    </linearGradient>
    <linearGradient id="photo-back" x1="0" y1="0" x2="1" y2="1">
      <stop offset="0" stop-color="#d9b48d"/>
      <stop offset="0.5" stop-color="#e3c29c"/>
      <stop offset="1" stop-color="#cfa57c"/>
    </linearGradient>
  </defs>
</svg>

<!-- Front side -->
<section class="flyer flyer--front">
  <svg class="flyer__bg" viewBox="0 0 496 1036" preserveAspectRatio="none">
    <rect width="496" height="1036" fill="var(--paper)"/>
    <rect y="160" width="496" height="420" fill="url(#photo-front)" role="img" aria-label="Photo: a therapist playing with a smiling young boy holding a teddy bear"/>
    <rect width="496" height="170" fill="var(--paper)" opacity="0.85"/>
    <polygon points="20,512 496,530 496,923 20,923" fill="var(--navy)"/>
    <polygon points="0,712 462,690 446,1036 0,1036" fill="var(--yellow)"/>
    <polygon points="48,906 496,923 496,1036 54,1036" fill="var(--teal)"/>
  </svg>

  <div class="brand">
    <span class="brand__mark"></span>
    <span class="brand__name">Bright Path Kids</span>
  </div>

  <h1 class="headline display">
    <span class="headline__small">Do you</span>
    <span class="headline__mid">have a verbal and able</span>
    <span class="headline__big">autistic child?</span>
  </h1>

  <h2 class="offer-title display">We offer:</h2>
  <ul class="bullets bullets--offer">
    <li><svg><use href="#icon-puzzle"/></svg>Specialist assessments</li>
    <li><svg><use href="#icon-puzzle"/></svg>Consultations for parents &amp; schools</li>
    <li><svg><use href="#icon-puzzle"/></svg>Social learning programmes</li>
    <li><svg><use href="#icon-puzzle"/></svg>Social-cognitive therapy</li>
  </ul>

  <div class="contact">
    <div class="contact__phone">
      <span class="contact__icon"><svg><use href="#icon-phone"/></svg></span>
      <span class="contact__number display">(09) 57-318-46</span>
    </div>
    <div class="contact__line"><svg><use href="#icon-mail"/></svg>info@brightpathkids.nz</div>
    <div class="contact__line"><svg viewBox="0 0 20 20"><use href="#icon-globe"/></svg>www.brightpathkids.nz</div>
  </div>
</section>

<!-- Back side -->
<section class="flyer flyer--back">
  <svg class="flyer__bg" viewBox="0 0 496 1036" preserveAspectRatio="none">
    <rect width="496" height="1036" fill="var(--yellow)"/>
    <polygon points="11,16 481,58 477,460 119,474 105,594 31,594" fill="var(--navy)"/>
    <polygon points="119,474 496,458 496,618 105,594" fill="var(--teal)"/>
    <rect x="0" y="878" width="496" height="158" fill="var(--white)"/>
    <rect x="486" y="596" width="10" height="282" fill="var(--white)"/>
    <rect x="5" y="596" width="481" height="282" fill="url(#photo-back)" role="img" aria-label="Photo: a young boy in a striped top playing with toy cars on a wooden floor"/>
  </svg>

  <h2 class="programmes-title display">Our programmes and<br>interventions include:</h2>
  <ul class="bullets bullets--programmes">
    <li><svg><use href="#icon-puzzle"/></svg>Chatter Quest</li>
    <li><svg><use href="#icon-puzzle"/></svg>Peer Bright</li>
    <li><svg><use href="#icon-puzzle"/></svg>Team Puzzles</li>
    <li><svg><use href="#icon-puzzle"/></svg>Tingle Words</li>
    <li><svg><use href="#icon-puzzle"/></svg>Pebble Tales</li>
    <li><svg><use href="#icon-puzzle"/></svg>Pembrook Speech Ladder</li>
    <li><svg><use href="#icon-puzzle"/></svg>Vorlin Method</li>
    <li><svg><use href="#icon-puzzle"/></svg>BRIMLE Method</li>
    <li><svg><use href="#icon-puzzle"/></svg>Tandem Pattern Coaching</li>
  </ul>

  <div class="contact">
    <div class="contact__phone">
      <span class="contact__icon"><svg><use href="#icon-phone"/></svg></span>
      <span class="contact__number display">(09) 57-318-46</span>
    </div>
    <div class="contact__line"><svg><use href="#icon-mail"/></svg>info@brightpathkids.nz</div>
    <div class="contact__line"><svg viewBox="0 0 20 20"><use href="#icon-globe"/></svg>www.brightpathkids.nz</div>
  </div>

  <div class="brand">
    <span class="brand__mark"></span>
    <span class="brand__name">Bright Path Kids</span>
  </div>
</section>

</body>
</html>
```